Brightford Lingua Partners, LLC

We need a business card that includes information about our business and conveys a reliable business that provides document translation services and interpreters for a variety of corporate and individual clients. We want to come across as professional, reliable, yet approachable. It should include the following on one side:

ESL / ENL Language Classes, Private Lessons, and Online Tutors
PALQE Training and Testing
Translating & Interpreting Services
Contact us about Over-the-Phone Interpreting in over 200 languages
24/7/365
www.brightfordlingua.example

The other side should include (555) 481-3062

Marla Quennick, President
412 Garvin Ave., Ste. 209
Indianapolis, IN 46999
Updates

Please add USA as part of the address. Also, please add mrqquennick@brightfordlinguapartners.example as the e-mail address. Thank you.

Target Market(s)

Business professionals, their families, the international community

Industry/Entity Type

Business

Contact Information for Business Card

24/7/365
www.brightfordlingua.example

(555) 481-3062

Marla Quennick, President
412 Garvin Ave., Ste. 209
Indianapolis, IN 46999
USA

Font styles to use
Sans Serif

Colors

Designer to choose colors to be used in the design.

Requirements
Must have
• See project description
• e-mail address and web address
• Phone number
Nice to have
• a globe
• physical address
Should not have
• Should not have the same color scheme as other agencies in our market in Indiana unless it is blue and black. No purple or yellow.

```html
<!DOCTYPE html>
<html lang="en">
<head>
<meta charset="utf-8">
<title>Brightford Lingua Partners – Business Card</title>
<link rel="stylesheet" href="https://fonts.googleapis.com/css2?family=Open+Sans:wght@400;600&display=swap">
<style>
  :root {
    --page-bg: #e6e6e6;
    --card-dark: #2f3134;
    --map-tone: #3a3d41;
    --card-light: #ffffff;
    --brand-blue: #1e94d2;
    --ink: #2b2b2b;
    --ink-soft: #4a4a4a;
    --on-dark: #f2f2f2;
  }
  * { box-sizing: border-box; margin: 0; padding: 0; }
  html, body { width: 1200px; height: 852px; overflow: hidden; }
  body {
    background: var(--page-bg);
    font-family: "Open Sans", Arial, sans-serif;
    position: relative;
  }
  .card {
    position: absolute;
    top: 271px;
    width: 540px;
    height: 310px;
    border-radius: 22px;
    overflow: hidden;
    box-shadow: 0 6px 18px rgba(0,0,0,0.18);
  }

  /* Services side */
  .card--services { left: 30px; background: var(--card-dark); color: var(--on-dark); }
  .world-map {
    position: absolute; left: 40px; top: 30px; width: 460px; height: 230px;
    background: radial-gradient(ellipse at center, var(--map-tone) 0%, var(--card-dark) 75%);
    border-radius: 40px;
  }
  .service-list {
    position: absolute; left: 0; right: 0; top: 46px;
    text-align: center; font-size: 16px; line-height: 25px; list-style: none;
  }
  .service-list .chev { color: var(--brand-blue); font-weight: 600; margin-right: 6px; }
  .service-list .chev--inline { margin-left: 14px; }
  .offer-note { position: absolute; left: 0; right: 0; top: 152px; }
  .divider { width: 250px; height: 1.5px; background: var(--brand-blue); margin: 8px auto 8px; }
  .otp-note { text-align: center; font-size: 16px; line-height: 24px; position: relative; }
  .services-web {
    position: absolute; left: 0; right: 0; bottom: 28px;
    text-align: center; font-size: 15px;
  }
  .accent { color: var(--brand-blue); }

  /* Contact side */
  .card--contact { left: 630px; background: var(--card-light); color: var(--ink); }
  .brand {
    position: absolute; right: 30px; top: 30px;
    display: flex; align-items: center; gap: 12px;
  }
  .brand-dot { width: 56px; height: 56px; border-radius: 50%; background: var(--brand-blue); flex: none; }
  .brand-name { font-size: 19px; font-weight: 600; line-height: 22px; color: var(--ink); }
  .person { position: absolute; left: 34px; top: 112px; }
  .person-name { font-size: 22px; font-weight: 600; color: var(--brand-blue); }
  .person-title { font-size: 13px; color: var(--ink-soft); margin-top: 2px; }
  .contact-list {
    position: absolute; right: 22px; top: 150px; list-style: none;
    font-size: 12px; line-height: 22px; color: var(--ink);
  }
  .contact-list li { display: flex; align-items: center; gap: 9px; white-space: nowrap; }
  .contact-list svg { width: 12px; height: 12px; fill: var(--ink-soft); flex: none; }
  .address { position: absolute; left: 34px; bottom: 34px; font-size: 14px; line-height: 21px; color: var(--ink); }
  .tagline-band {
    position: absolute; right: 0; bottom: 22px; width: 300px; height: 46px;
    background: var(--brand-blue); color: #fff;
    clip-path: polygon(14px 0, 100% 0, 100% 100%, 0 100%, 0 14px);
    display: flex; align-items: center; justify-content: center;
    font-size: 12.5px; white-space: nowrap;
  }
  .base-strip { position: absolute; left: 0; right: 0; bottom: 0; height: 22px; background: var(--card-dark); }
</style>
</head>
<body>

<section class="card card--services" aria-label="Services side">
  <div class="world-map" role="img" aria-label="Faint world map in dark grey tones"></div>
  <ul class="service-list">
    <li><span class="chev">»</span>ESL / ENL Language Classes</li>
    <li><span class="chev">»</span>Private Lessons <span class="chev chev--inline">»</span>Online Tutors</li>
    <li><span class="chev">»</span>PALQE Training and Testing</li>
    <li><span class="chev">»</span>Translating &amp; Interpreting Services</li>
  </ul>
  <div class="offer-note">
    <div class="divider"></div>
    <p class="otp-note">Contact us about Over-the-Phone<br>Interpreting in over 200 languages<br>24/7/365</p>
  </div>
  <p class="services-web">www.<span class="accent">brightfordlingua</span>.example</p>
</section>

<section class="card card--contact" aria-label="Contact side">
  <div class="brand">
    <span class="brand-dot"></span>
    <span class="brand-name">Brightford Lingua<br>Partners LLC</span>
  </div>

  <div class="person">
    <p class="person-name">Marla Quennick</p>
    <p class="person-title">President</p>
  </div>

  <ul class="contact-list">
    <li>
      <svg viewBox="0 0 24 24" aria-hidden="true"><path d="M6.6 10.8a15.1 15.1 0 0 0 6.6 6.6l2.2-2.2c.3-.3.7-.4 1-.2 1.1.4 2.3.6 3.6.6.6 0 1 .4 1 1V20c0 .6-.4 1-1 1A17 17 0 0 1 3 4c0-.6.4-1 1-1h3.5c.6 0 1 .4 1 1 0 1.3.2 2.5.6 3.6.1.3 0 .7-.2 1z"/></svg>
      <span>(555) 481-3062</span>
    </li>
    <li>
      <svg viewBox="0 0 24 24" aria-hidden="true"><path d="M2 5h20v14H2zm2 2v.5l8 5 8-5V7zm0 2.8V17h16V9.8l-8 5z"/></svg>
      <span>mrqquennick@brightfordlinguapartners.example</span>
    </li>
    <li>
      <svg viewBox="0 0 24 24" aria-hidden="true"><path d="M12 2a10 10 0 1 0 0 20 10 10 0 0 0 0-20zm6.9 9h-3a15 15 0 0 0-1.3-5.6A8 8 0 0 1 18.9 11zM12 4c.9 1.3 1.7 3.8 1.9 7h-3.8c.2-3.2 1-5.7 1.9-7zM9.4 5.4A15 15 0 0 0 8.1 11h-3a8 8 0 0 1 4.3-5.6zM5.1 13h3a15 15 0 0 0 1.3 5.6A8 8 0 0 1 5.1 13zm6.9 7c-.9-1.3-1.7-3.8-1.9-7h3.8c-.2 3.2-1 5.7-1.9 7zm2.6-1.4a15 15 0 0 0 1.3-5.6h3a8 8 0 0 1-4.3 5.6z"/></svg>
      <span>www.<span class="accent">brightfordlingua</span>.example</span>
    </li>
  </ul>

  <p class="address">412 Garvin Ave., Ste. 209<br>Indianapolis, IN 46999 USA</p>

  <div class="tagline-band">Interpreting | Translating | Language Training</div>
  <div class="base-strip"></div>
</section>

</body>
</html>
```